Wedding and event Photography company.

We need a business card design for a photography company based in Singapore named TamKeza. Our core service offering is wedding photojournalism. We would like to see minimalistic designs that use the colour white. The final design should communicate a sense of ease and reliability.

The attached are a couple of visual reference which i found over the web, i hope it will helps.

Project Brief Update (14th July 2014):
- Please refrain from using any images from the website for the design. The laws and regulations over here does not allow me to distribute my client's images. Thanks!

Target Market(s)

Young and middle aged adults aged 24 - 38. With money to spend =D

Industry/Entity Type

Business

Contact Information for Business Card

Name: Dev Lunor
Designation: Head Photographer
Mobile: +65 81749026
Email: jun@tamkeza.example
Website: www.tamkeza.example

Font styles to use
Other font styles liked:
• Baskerville URW

Colors

Designer to choose colors to be used in the design.

Requirements
Must have
• Must include:
• - The brand TamKeza
• - The logo attached
• - Please help to place the brand TamKeza with the logo according to your preferences.
• - Services
• - Wedding Photography
• - Portraiture
• - Photojournalism
Nice to have
• Looking forward to an elegant and simple design. Please see attached examples!
• Please use Serif Fonts
Should not have
• Please refrain from using dark tones for the majority of the design.
• Please refrain from letterpress and embossing.

```html
<!DOCTYPE html>
<html lang="en">
<head>
<meta charset="utf-8">
<title>TamKeza Business Card</title>
<link href="https://fonts.googleapis.com/css2?family=Libre+Baskerville:wght@400;700&display=swap" rel="stylesheet">
<style>
  :root {
    --backdrop: #e9e7e4;
    --card: #ffffff;
    --facet-light: #fbfbfb;
    --facet-mid: #f3f3f3;
    --facet-dark: #ececec;
    --ink: #151515;
    --ink-soft: #3c3c3c;
    --icon: #8a8a8a;
    --shadow: rgba(0,0,0,0.14);
  }
  * { margin: 0; padding: 0; box-sizing: border-box; }
  html, body { width: 1200px; height: 900px; overflow: hidden; }
  body {
    background: var(--backdrop);
    font-family: "Libre Baskerville", "Baskerville", serif;
    color: var(--ink);
    position: relative;
  }
  .card {
    position: absolute;
    left: 320px;
    width: 560px;
    height: 320px;
    background: var(--card);
    box-shadow: 0 10px 28px var(--shadow);
    overflow: hidden;
  }
  .card--front { top: 100px; }
  .card--back { top: 480px; }
  .card__facets { position: absolute; inset: 0; width: 100%; height: 100%; }
  .card__content {
    position: absolute; inset: 0;
    display: flex; flex-direction: column; align-items: center; justify-content: center;
    text-align: center;
  }
  .brand {
    display: flex; align-items: center; gap: 10px;
    font-size: 26px; font-weight: 400; letter-spacing: 1px; color: var(--ink);
  }
  .brand__dot { width: 12px; height: 12px; border-radius: 50%; background: var(--ink); }
  .card--front .brand { margin-bottom: 18px; }
  .card--back .brand { font-size: 40px; gap: 14px; }
  .card--back .brand__dot { width: 16px; height: 16px; }
  .person__name { font-size: 26px; letter-spacing: 0.5px; }
  .person__title { font-size: 13px; color: var(--ink-soft); margin-top: 4px; }
  .contact {
    display: flex; gap: 28px; margin-top: 18px;
    font-size: 13px; color: var(--ink-soft);
  }
  .contact__item { display: flex; align-items: center; gap: 7px; }
  .contact__icon { width: 16px; height: 16px; }
  .services__label { margin-top: 18px; font-size: 13px; color: var(--ink); }
  .services__list { margin-top: 5px; font-size: 11px; color: var(--ink-soft); letter-spacing: 0.3px; }
  .website {
    margin-top: 26px; font-size: 14px; letter-spacing: 1.5px; color: var(--ink);
  }
</style>
</head>
<body>

<section class="card card--front">
  <svg class="card__facets" viewBox="0 0 560 320" preserveAspectRatio="none" aria-hidden="true">
    <polygon points="0,0 560,0 280,160" fill="var(--facet-mid)"/>
    <polygon points="560,0 560,320 280,160" fill="var(--facet-dark)"/>
    <polygon points="0,320 560,320 280,160" fill="var(--facet-light)"/>
    <polygon points="0,0 0,320 280,160" fill="var(--card)"/>
  </svg>
  <div class="card__content">
    <div class="brand"><span class="brand__dot"></span>TamKeza</div>
    <div class="person__name">Dev Lunor</div>
    <div class="person__title">Head Photographer</div>
    <div class="contact">
      <span class="contact__item">
        <svg class="contact__icon" viewBox="0 0 16 16" aria-hidden="true">
          <circle cx="8" cy="8" r="8" fill="var(--icon)"/>
          <rect x="5.5" y="3.5" width="5" height="9" rx="1" fill="#fff"/>
          <rect x="6.5" y="4.8" width="3" height="5.5" fill="var(--icon)"/>
        </svg>+65 81749026
      </span>
      <span class="contact__item">
        <svg class="contact__icon" viewBox="0 0 16 16" aria-hidden="true">
          <circle cx="8" cy="8" r="8" fill="var(--icon)"/>
          <rect x="4" y="5" width="8" height="6" fill="#fff"/>
          <polyline points="4,5 8,8.5 12,5" fill="none" stroke="var(--icon)" stroke-width="1"/>
        </svg>jun@tamkeza.example
      </span>
    </div>
    <div class="services__label">Services</div>
    <div class="services__list">Wedding Photography • Portraiture • Photojournalism</div>
  </div>
</section>

<section class="card card--back">
  <svg class="card__facets" viewBox="0 0 560 320" preserveAspectRatio="none" aria-hidden="true">
    <polygon points="0,0 560,0 280,160" fill="var(--facet-mid)"/>
    <polygon points="560,0 560,320 280,160" fill="var(--facet-dark)"/>
    <polygon points="0,320 560,320 280,160" fill="var(--facet-light)"/>
    <polygon points="0,0 0,320 280,160" fill="var(--card)"/>
  </svg>
  <div class="card__content">
    <div class="brand"><span class="brand__dot"></span>TamKeza</div>
    <div class="website">WWW.TAMKEZA.EXAMPLE</div>
  </div>
</section>

</body>
</html>
```